TRV Business Card

Business card design for a handyman company. Want to portray a professional image and stay away from the "Mom & Pops" image that is normally associated with handyman companies.

Business

```html
<!DOCTYPE html>
<html lang="en">
<head>
<meta charset="utf-8">
<title>TRV Business Card</title>
<link rel="stylesheet" href="https://fonts.googleapis.com/css2?family=Exo+2:wght@400;700&display=swap">
<style>
  :root {
    --bg: #e9e7e4;
    --card: #ffffff;
    --navy: #0f2747;
    --accent: #2f3f9e;
    --ink: #2a2f3a;
    --ink-soft: #4a505c;
    --light: #ffffff;
  }
  * { margin: 0; padding: 0; box-sizing: border-box; }
  html, body { width: 1200px; height: 867px; overflow: hidden; }
  body {
    background: var(--bg);
    font-family: "Exo 2", sans-serif;
    position: relative;
  }
  .business-card {
    position: absolute;
    left: 180px;
    top: 193px;
    width: 840px;
    height: 480px;
    background: var(--card);
    box-shadow: 0 10px 30px rgba(0,0,0,0.18);
    overflow: hidden;
  }
  .card-shape {
    position: absolute;
    inset: 0;
    width: 100%;
    height: 100%;
  }
  .shape-navy { fill: var(--navy); }
  .shape-accent { fill: var(--accent); }
  .brand {
    position: absolute;
    left: 46px;
    top: 52px;
  }
  .brand-name {
    font-weight: 700;
    font-size: 40px;
    color: var(--navy);
    letter-spacing: 1px;
  }
  .contact-list {
    position: absolute;
    left: 42px;
    top: 258px;
    list-style: none;
    font-size: 19px;
    line-height: 30px;
    color: var(--ink-soft);
  }
  .website {
    position: absolute;
    left: 42px;
    top: 366px;
    font-size: 20px;
    color: var(--ink);
  }
  .address {
    position: absolute;
    left: 42px;
    top: 432px;
    font-size: 19px;
    color: var(--ink-soft);
  }
  .service-list {
    position: absolute;
    left: 555px;
    top: 292px;
    list-style: none;
    font-size: 23px;
    line-height: 40px;
    color: var(--light);
  }
  .service-list li {
    display: flex;
    align-items: center;
    gap: 14px;
  }
  .service-list li::before {
    content: "";
    width: 15px;
    height: 15px;
    border-radius: 50%;
    background: var(--light);
    flex: none;
  }
</style>
</head>
<body>
  <article class="business-card">
    <svg class="card-shape" viewBox="0 0 840 480" preserveAspectRatio="none" aria-hidden="true">
      <path class="shape-navy" d="M672,0 L840,0 L840,480 L440,480 C530,360 630,190 672,0 Z"/>
      <path class="shape-accent" d="M640,0 L660,0 C615,190 515,360 430,480 L420,480 C500,360 598,190 640,0 Z"/>
    </svg>

    <div class="brand">
      <span class="brand-name">TRV Home Services</span>
    </div>

    <ul class="contact-list">
      <li>P: (555) 318-0427</li>
      <li>F: (555) 318-0429</li>
      <li>E: info@TrvHomeServices.com</li>
    </ul>
    <p class="website">www.TrvHomeServices.com</p>
    <p class="address">418 Elm Grove Rd, Fairview, Ks 66000</p>

    <ul class="service-list">
      <li>Home Repairs</li>
      <li>Handyman Services</li>
      <li>Drain Cleaning</li>
      <li>Carpet Cleaning</li>
    </ul>
  </article>
</body>
</html>
```